International horse riding portal needs web design

We are looking for the web design for the new "Feldmoor" web portal.

Offers from the world of horses and riding should be found on this portal, eg from the categories riding schools, riding holidays, farriers, riding stables, riding stables. And all information about riding.

It is important that the different areas can be found easily and clearly. For some categories, some features should already be available in the search bar.

In addition, the design should make you want to go horse riding. The user should be emotionally picked up on the landing page.

In the lower area, some offers should be advertised, eg from the areas of riding holidays, riding training, and horse trading.

Please use the colors from the logo for the design.
C100 M50 Y10 K50 and C0 M20 Y60 K30

```html
<!DOCTYPE html>
<html lang="en">
<head>
<meta charset="utf-8">
<title>Feldmoor – Horse Riding Portal</title>
<link href="https://fonts.googleapis.com/css2?family=Inter:wght@400;500;600;700&family=Noto+Serif:wght@400;500&display=swap" rel="stylesheet">
<style>
:root{
  --navy:#0f3d6b;
  --navy-dark:#0b325a;
  --gold:#b8965a;
  --gold-light:#d9c39a;
  --ink:#333a44;
  --muted:#6b717a;
  --grey-bg:#efefef;
  --line:#d8d2c4;
  --white:#ffffff;
}
*{margin:0;padding:0;box-sizing:border-box}
html,body{width:1200px;height:3620px;overflow:hidden;background:var(--white)}
body{position:relative;font-family:"Inter",sans-serif;color:var(--ink)}
.abs{position:absolute}
.serif{font-family:"Noto Serif",serif}
.gold{color:var(--gold)}
.navy{color:var(--navy)}

/* header */
.site-header{position:absolute;left:0;top:0;width:1200px;height:129px;background:var(--white);box-shadow:0 2px 6px rgba(0,0,0,.08);z-index:5}
.brand{position:absolute;left:112px;top:62px;font-family:"Noto Serif",serif;font-size:32px;color:var(--navy);letter-spacing:1px}
.brand-dot{position:absolute;left:166px;top:4px;width:56px;height:56px;border-radius:50%;background:var(--gold)}
.search{position:absolute;left:329px;top:15px;width:362px;height:45px;border:1.5px solid var(--navy);border-radius:23px;font-size:13px;color:var(--muted);padding:13px 20px}
.search svg{position:absolute;right:18px;top:12px}
.util{position:absolute;top:8px;font-size:12px;font-weight:500;color:var(--navy);text-align:center;width:90px}
.util svg{display:block;margin:0 auto 6px}
.login{position:absolute;left:1012px;top:0;width:86px;height:58px;background:var(--gold);color:var(--white);font-size:12px;font-weight:600;text-align:center;padding-top:10px}
.login svg{display:block;margin:0 auto 4px}
.main-nav{position:absolute;top:90px;font-size:15px;font-weight:500;color:#1d2230;letter-spacing:.2px}
.main-nav span::after{content:"";display:inline-block;width:6px;height:6px;border-right:1.5px solid var(--navy);border-bottom:1.5px solid var(--navy);transform:rotate(45deg);margin-left:7px;position:relative;top:-3px}

/* hero */
.hero{position:absolute;left:0;top:129px;width:1200px;height:670px;background:linear-gradient(180deg,#7fa9d0 0%,#b6cfe2 40%,#8aa264 62%,#5f7c3a 78%,#c9b79a 100%)}
.hero-rider{position:absolute;left:520px;top:0;width:600px;height:600px;background:radial-gradient(ellipse at 55% 50%,rgba(60,40,30,.55),rgba(60,40,30,0) 65%)}
.welcome{position:absolute;left:117px;top:315px;font-family:"Noto Serif",serif;font-size:42px;color:var(--gold);letter-spacing:.5px}
.hero-title{position:absolute;left:114px;top:355px;font-family:"Noto Serif",serif;font-size:82px;color:var(--navy);letter-spacing:1px}
.tabs{position:absolute;left:124px;top:492px;display:flex;gap:6px}
.tab{height:40px;padding:12px 24px 0;font-size:13px;font-weight:700;color:var(--navy);background:#e7dcc6;text-transform:uppercase}
.tab.active{background:var(--white)}
.finder{position:absolute;left:124px;top:532px;width:886px;height:88px;background:var(--white);padding:0 0 0 30px;display:flex;align-items:center}
.radio{font-size:14px;color:var(--navy);margin-right:26px;display:flex;align-items:center}
.radio i{width:14px;height:14px;border:1.5px solid var(--navy);border-radius:50%;margin-right:7px;position:relative}
.radio i.on::after{content:"";position:absolute;left:2.5px;top:2.5px;width:6px;height:6px;border-radius:50%;background:var(--navy)}
.zip{margin-left:0;width:207px;height:40px;border:1px solid #cfd4da;font-size:12px;color:var(--muted);display:flex;align-items:center;padding-left:12px;gap:6px}
.find{width:86px;height:40px;background:var(--navy);color:var(--white);font-size:14px;font-weight:700;display:flex;align-items:center;justify-content:center}

/* intro */
.section-title{position:absolute;left:0;width:1200px;text-align:center;font-family:"Noto Serif",serif;color:var(--navy)}
.rule{position:absolute;height:2px;background:var(--gold)}
.intro-text{position:absolute;top:957px;width:445px;font-size:15px;line-height:24.5px;color:#2c2f35}

/* categories */
.cat{position:absolute;top:1117px;width:183px;text-align:center}
.cat-label{position:absolute;top:1350px;font-size:17px;font-weight:700;letter-spacing:.3px;text-align:center;width:240px}
.cat-label b{color:var(--navy)}
.cat-label span{color:var(--gold)}
.chev{position:absolute}

/* cards */
.card{position:absolute;top:1597px;width:307px;height:405px;border:1px solid #b8bfc8;background:var(--white)}
.card-img{height:213px;border-top-right-radius:70px;border-bottom-left-radius:70px}
.card h3{margin:24px 0 0 32px;font-size:17px;font-weight:600;color:var(--navy);line-height:21px;width:240px}
.card p{margin:14px 0 0 32px;font-size:13px;line-height:20px;color:var(--muted);width:250px}
.btn{display:inline-flex;align-items:center;background:var(--gold);color:var(--white);font-weight:600;text-transform:uppercase}
.card .btn{margin:14px 0 0 32px;height:34px;padding:0 18px;font-size:11px}

/* training */
.training{position:absolute;left:0;top:2096px;width:1200px;height:515px;background:var(--grey-bg);overflow:hidden}
.training-text{position:absolute;left:128px;top:2285px;width:440px;font-size:15px;line-height:28px;color:#2c2f35}

/* horses */
.horse{position:absolute;top:2790px;width:263px;height:276px}
.horse-feature{position:absolute;left:346px;top:2771px;width:263px;height:313px;background:linear-gradient(160deg,#2a1c14,#5a3320 55%,#1a120d);box-shadow:0 10px 24px rgba(0,0,0,.35)}
.horse-caption{position:absolute;left:0;bottom:0;width:100%;height:60px;border-top:1px solid rgba(255,255,255,.35);color:var(--white)}

/* footer */
.footer{position:absolute;left:0;top:3120px;width:1200px;height:500px}
.foot-h{position:absolute;top:3288px;font-family:"Noto Serif",serif;font-size:19px;color:var(--white);letter-spacing:.3px}
.foot-links{position:absolute;left:358px;top:3336px;font-size:12px;font-weight:600;color:var(--white);line-height:29px}
.contact-row{position:absolute;left:562px;font-size:12px;font-weight:600;color:var(--white);line-height:20px}
.contact-row svg{position:absolute;left:0;top:2px}
.contact-row div{margin-left:36px}
.email-in{position:absolute;left:865px;top:3338px;width:208px;height:32px;background:var(--white);font-size:10px;color:var(--muted);padding:10px 14px}
.subscribe{position:absolute;left:865px;top:3379px;width:208px;height:33px;background:var(--gold);color:var(--white);font-size:12px;font-weight:700;display:flex;align-items:center;justify-content:center}
.social{position:absolute;top:3430px;width:22px;height:22px;border-radius:50%;border:2px solid var(--white)}
.copyright{position:absolute;left:0;top:3578px;width:1200px;text-align:center;font-size:13px;color:var(--white)}
</style>
</head>
<body>

<!-- header -->
<header class="site-header">
  <div class="brand-dot"></div>
  <div class="brand">FELDMOOR</div>
  <div class="search">Search &gt; Feature
    <svg width="20" height="20" viewBox="0 0 20 20"><circle cx="8" cy="8" r="6" fill="none" stroke="#0f3d6b" stroke-width="2.5"/><path d="M12.5 12.5 18 18" stroke="#0f3d6b" stroke-width="2.5" stroke-linecap="round"/></svg>
  </div>
  <div class="util" style="left:717px"><svg width="20" height="20" viewBox="0 0 20 20"><rect x="3" y="2" width="14" height="16" fill="none" stroke="#b8965a" stroke-width="1.5"/><path d="M6 6h8M6 10h8M6 14h5" stroke="#b8965a" stroke-width="1.5"/></svg>NEWS</div>
  <div class="util" style="left:812px"><svg width="20" height="20" viewBox="0 0 20 20"><path d="M4 2v8a6 6 0 0 0 12 0V2" fill="none" stroke="#b8965a" stroke-width="2"/></svg>RESOURCES</div>
  <div class="util" style="left:910px"><svg width="20" height="20" viewBox="0 0 20 20"><path d="M3 4h2M8 4h10M3 10h2M8 10h10M3 16h2M8 16h10" stroke="#b8965a" stroke-width="2"/></svg>MY LIST</div>
  <div class="login"><svg width="20" height="20" viewBox="0 0 20 20"><circle cx="10" cy="6" r="4" fill="none" stroke="#fff" stroke-width="1.5"/><path d="M3 19c0-4 3-7 7-7s7 3 7 7z" fill="none" stroke="#fff" stroke-width="1.5"/></svg>LOGIN</div>
  <nav>
    <div class="main-nav" style="left:332px"><span>ABOUT US</span></div>
    <div class="main-nav" style="left:452px"><span>RIDING SCHOOL</span></div>
    <div class="main-nav" style="left:604px"><span>RIDING HOLIDAYS</span></div>
    <div class="main-nav" style="left:769px"><span>FARRIES</span></div>
    <div class="main-nav" style="left:871px"><span>RIDING STABLES</span></div>
    <div class="main-nav" style="left:1031px">CONTACT</div>
  </nav>
</header>

<!-- hero -->
<section class="hero" role="img" aria-label="Photo of a woman riding a dark bay horse across a green paddock under a blue sky">
  <div class="hero-rider"></div>
</section>
<svg class="abs" style="left:0;top:680px" width="1200" height="120" viewBox="0 0 1200 120">
  <path d="M0 120 L0 70 C250 20 550 10 780 40 C950 60 1080 60 1200 30 L1200 120 Z" fill="#fff"/>
  <path d="M0 110 C200 20 560 0 800 40 C950 62 1080 60 1200 30 L1200 42 C1080 78 950 78 790 56 C560 20 220 40 0 110Z" fill="#b8965a"/>
  <path d="M600 24 C700 26 760 35 830 46 C960 66 1080 60 1200 28 L1200 48 C1080 84 940 84 800 60 C740 50 680 34 600 24Z" fill="#0f3d6b"/>
</svg>
<div class="welcome">WELCOME TO</div>
<h1 class="hero-title" style="font-weight:400">FELDMOOR</h1>
<div class="tabs">
  <div class="tab active">Riding School</div>
  <div class="tab" style="margin-left:0">Riding Holidays</div>
  <div class="tab">Farries</div>
  <div class="tab">Riding Stables</div>
</div>
<div class="finder">
  <div class="radio"><i class="on"></i>Feature First</div>
  <div class="radio"><i></i>Feature Second</div>
  <div class="radio"><i></i>Feature Third</div>
  <div class="radio"><i></i>Feature Fourth</div>
  <div class="zip"><svg width="10" height="14" viewBox="0 0 10 14"><path d="M5 0a5 5 0 0 0-5 5c0 4 5 9 5 9s5-5 5-9a5 5 0 0 0-5-5z" fill="#0f3d6b"/><circle cx="5" cy="5" r="2" fill="#fff"/></svg>Zip Code/ City</div>
  <div class="find">FIND</div>
</div>

<!-- intro -->
<h2 class="section-title" style="top:832px;font-size:30px;line-height:37px;font-weight:400">IHIC TECTIO BLAB INCIENIS AUT HILIQUO QUISQUI<br>AEPRECTUR? URESEQUOD QUI DITIS</h2>
<div class="rule" style="left:552px;top:916px;width:80px"></div>
<p class="intro-text" style="left:119px">Lorem ipsum dolor sit amet, consectetur adipiscing elit, sed do eiusmod tempor incididunt ut labore et dolore magna aliqua. Ut enim ad minim.Lorem ipsum dolor sit amet.Lorem ipsum dolor sit amet, consectetur adipiscing.</p>
<p class="intro-text" style="left:617px">Lorem ipsum dolor sit amet, consectetur adipiscing elit, sed do eiusmod tempor incididunt ut labore et dolore magna aliqua. Ut enim ad minim.Lorem ipsum dolor sit amet.Lorem ipsum dolor sit amet, consectetur adipiscing.</p>

<!-- categories -->
<svg class="chev" style="left:68px;top:1202px" width="20" height="32" viewBox="0 0 20 32"><path d="M17 2 4 16l13 14" fill="none" stroke="#b8965a" stroke-width="3"/></svg>
<svg class="chev" style="left:1124px;top:1202px" width="20" height="32" viewBox="0 0 20 32"><path d="M3 2l13 14L3 30" fill="none" stroke="#b8965a" stroke-width="3"/></svg>

<svg class="cat" style="left:105px" height="215" viewBox="0 0 183 215" role="img" aria-label="Photo of a rider hugging her horse"><defs><linearGradient id="g1" x1="0" y1="0" x2="0" y2="1"><stop offset="0" stop-color="#9aa08e"/><stop offset="1" stop-color="#5e5a4c"/></linearGradient></defs><path d="M91.5 215C62 178 0 145 0 91.5a91.5 91.5 0 0 1 183 0C183 145 121 178 91.5 215Z" fill="url(#g1)"/></svg>
<svg class="cat" style="left:309px" height="215" viewBox="0 0 183 215" role="img" aria-label="Photo of a rider on a chestnut horse against the sky"><defs><linearGradient id="g2" x1="0" y1="0" x2="0" y2="1"><stop offset="0" stop-color="#a9c8e4"/><stop offset="1" stop-color="#8a5632"/></linearGradient></defs><path d="M91.5 215C62 178 0 145 0 91.5a91.5 91.5 0 0 1 183 0C183 145 121 178 91.5 215Z" fill="url(#g2)"/></svg>
<svg class="cat" style="left:515px" height="215" viewBox="0 0 183 215" role="img" aria-label="Photo of a rider jumping on a bay horse"><defs><linearGradient id="g3" x1="0" y1="0" x2="0" y2="1"><stop offset="0" stop-color="#b3cfe6"/><stop offset="1" stop-color="#6a4026"/></linearGradient></defs><path d="M91.5 215C62 178 0 145 0 91.5a91.5 91.5 0 0 1 183 0C183 145 121 178 91.5 215Z" fill="url(#g3)"/></svg>
<svg class="cat" style="left:718px" height="215" viewBox="0 0 183 215" role="img" aria-label="Photo of a horse looking out of a stable stall"><defs><linearGradient id="g4" x1="0" y1="0" x2="0" y2="1"><stop offset="0" stop-color="#8b6a4e"/><stop offset="1" stop-color="#4a3020"/></linearGradient></defs><path d="M91.5 215C62 178 0 145 0 91.5a91.5 91.5 0 0 1 183 0C183 145 121 178 91.5 215Z" fill="url(#g4)"/></svg>
<svg class="cat" style="left:923px" height="215" viewBox="0 0 183 215" role="img" aria-label="Photo of riders on a woodland trail"><defs><linearGradient id="g5" x1="0" y1="0" x2="0" y2="1"><stop offset="0" stop-color="#6f8a4e"/><stop offset="1" stop-color="#c7a9a0"/></linearGradient></defs><path d="M91.5 215C62 178 0 145 0 91.5a91.5 91.5 0 0 1 183 0C183 145 121 178 91.5 215Z" fill="url(#g5)"/></svg>

<div class="cat-label" style="left:76px"><span>RIDING</span> <b>SCHOOLS</b></div>
<div class="cat-label" style="left:275px"><span>RIDING</span> <b>HOLIDAYS</b></div>
<div class="cat-label" style="left:489px"><span>RIDING</span> <b>FARRIERS</b></div>
<div class="cat-label" style="left:689px"><span>RIDING</span> <b>STABLES</b></div>
<div class="cat-label" style="left:905px"><span>ABOUT</span> <b>RIDING</b></div>

<!-- offers -->
<div class="abs" style="left:124px;top:1457px;width:946px;height:1px;background:var(--line)"></div>
<div class="abs" style="left:588px;top:1448px;width:20px;height:20px;border-radius:50%;background:var(--navy)"></div>
<h2 class="section-title" style="top:1510px;font-size:35px;font-weight:400">IHIC TECTIO BLAB <span class="gold">INCIENIS AUT</span></h2>

<svg class="chev" style="left:66px;top:1782px" width="20" height="34" viewBox="0 0 20 34"><path d="M17 2 4 17l13 15" fill="none" stroke="#b8bfc8" stroke-width="3"/></svg>
<svg class="chev" style="left:1106px;top:1782px" width="20" height="34" viewBox="0 0 20 34"><path d="M3 2l13 15L3 32" fill="none" stroke="#b8965a" stroke-width="3"/></svg>

<article class="card" style="left:124px">
  <div class="card-img" role="img" aria-label="Photo of a rider on a chestnut horse in a forest" style="background:linear-gradient(160deg,#3f6a2c,#8fae4a 50%,#7a4a24)"></div>
  <h3>Neque porro quisquam est qui dolorem ipsum qui</h3>
  <p>Lorem ipsum dolor sit amet, consect-etur adipiscing elit, sed eiusmod</p>
  <span class="btn">Learn More ›</span>
</article>
<article class="card" style="left:447px">
  <div class="card-img" role="img" aria-label="Photo of a woman stroking a dark horse at sunset" style="background:linear-gradient(160deg,#c98a26,#e9b94a 50%,#4a3422)"></div>
  <h3>Sed ut perspiciatis unde omnis iste natus error sit</h3>
  <p>Lorem ipsum dolor sit amet, consect-etur adipiscing elit, sed eiusmod</p>
  <span class="btn">Learn More ›</span>
</article>
<article class="card" style="left:771px">
  <div class="card-img" role="img" aria-label="Photo of a smiling woman hugging a black horse in a paddock" style="background:linear-gradient(160deg,#2a2a2a,#8a7f75 45%,#e2d9cd)"></div>
  <h3>Neque porro quisquam est qui dolorem ipsum qui</h3>
  <p>Lorem ipsum dolor sit amet, consect-etur adipiscing elit, sed eiusmod</p>
  <span class="btn">Learn More ›</span>
</article>

<!-- training -->
<section class="training">
  <svg class="abs" style="left:580px;top:0" width="620" height="515" viewBox="0 0 620 515">
    <defs><linearGradient id="gt" x1="0" y1="0" x2="1" y2="1"><stop offset="0" stop-color="#c9b596"/><stop offset=".5" stop-color="#a4663c"/><stop offset="1" stop-color="#ece4da"/></linearGradient></defs>
    <path d="M150 0H620V515H120C40 440 10 360 10 260C10 150 60 60 150 0Z" fill="url(#gt)" role="img" aria-label="Photo of a young woman resting her head against a chestnut horse"/>
    <path d="M150 0C60 60 10 150 10 260C10 360 40 440 120 515" fill="none" stroke="#0f3d6b" stroke-width="7" stroke-dasharray="330 900"/>
    <path d="M10 270C12 360 45 440 120 515" fill="none" stroke="#b8965a" stroke-width="7"/>
  </svg>
  <h2 class="abs serif" style="left:128px;top:104px;font-size:35px;font-weight:400;color:var(--navy)">HORSE RIDING <span class="gold">TRAINING</span></h2>
  <div class="rule" style="left:128px;top:152px;width:60px"></div>
</section>
<p class="training-text">Lorem ipsum dolor sit amet, consectetur adipiscing elit, sed do eiusmod tempor incididunt ut labore et Aolore magna aliqua. Ut enim ad minim veniam, quis nos-trud exercitation ullamco laboris nisi ut aliquip ex ea com-modo consequatmagna aliquaenim ad minim.</p>
<span class="btn abs" style="left:128px;top:2439px;width:162px;height:46px;justify-content:center;font-size:14px">Learn More ›</span>

<!-- horses -->
<h2 class="section-title" style="top:2670px;font-size:40px;font-weight:400">OUR <span class="gold">HORSES</span></h2>
<div class="rule" style="left:568px;top:2726px;width:80px"></div>
<div class="horse" style="left:72px;background:linear-gradient(160deg,#d8b37a,#a5501f 55%,#6f8a3a)" role="img" aria-label="Photo of a chestnut horse with a flowing mane"></div>
<div class="horse-feature" role="img" aria-label="Photo of a bay horse wearing a halter">
  <div class="horse-caption">
    <div class="abs" style="left:18px;top:16px;font-size:19px;font-weight:600">Horse Name</div>
    <div class="abs" style="left:163px;top:12px;font-size:10px;line-height:18px"><b>Birth Year:</b> 2018<br><b>Gender:</b> Gelding</div>
  </div>
</div>
<div class="horse" style="left:621px;background:linear-gradient(180deg,#7d8fa4,#3a4a3a 45%,#1e1a1a 65%,#c8321f)" role="img" aria-label="Photo of a black horse standing in a field of red poppies"></div>
<div class="horse" style="left:895px;background:linear-gradient(160deg,#a4b85a,#a9602a 50%,#dfe38a)" role="img" aria-label="Photo of a bay horse trotting across a sunny meadow"></div>

<!-- footer -->
<footer class="footer">
  <svg class="abs" style="left:0;top:0" width="1200" height="500" viewBox="0 0 1200 500">
    <path d="M0 20C200 110 450 80 700 60C900 45 1060 60 1200 110V500H0Z" fill="#0f3d6b"/>
    <path d="M0 0C200 100 450 70 700 52C900 38 1060 50 1200 95V110C1060 62 900 48 700 62C450 82 200 110 0 22Z" fill="#b8965a"/>
    <path d="M0 443H1200" stroke="rgba(255,255,255,.2)"/>
  </svg>
</footer>
<div class="abs" style="left:182px;top:3292px;width:52px;height:52px;border-radius:50%;background:var(--white)"></div>
<div class="abs serif" style="left:114px;top:3350px;font-size:32px;color:var(--white);letter-spacing:1px">FELDMOOR</div>

<div class="foot-h" style="left:358px">NAVIGATION</div>
<div class="foot-links">About Us<br>Riding School<br>Riding Holidays<br>Farries<br>Riding Stables</div>

<div class="foot-h" style="left:562px">CONTACT US</div>
<div class="contact-row" style="top:3341px"><svg width="18" height="22" viewBox="0 0 18 22"><path d="M9 0a8 8 0 0 0-8 8c0 6 8 14 8 14s8-8 8-14a8 8 0 0 0-8-8z" fill="#fff"/><circle cx="9" cy="8" r="3" fill="#0f3d6b"/></svg><div>482 Larkspur Avenue P.O. Box 92<br>Westbrook, Ontario K7L 3P4</div></div>
<div class="contact-row" style="top:3389px"><svg width="22" height="20" viewBox="0 0 22 20"><path d="M4 1l4 4-2 3c1 3 4 6 7 7l3-2 4 4-3 3C9 19 2 12 1 4z" fill="#fff"/></svg><div>Tel: (555) 214-7390</div></div>
<div class="contact-row" style="top:3421px"><svg width="22" height="16" viewBox="0 0 22 16"><rect x="1" y="1" width="20" height="14" fill="none" stroke="#fff" stroke-width="2"/><path d="M1 1l10 8 10-8" fill="none" stroke="#fff" stroke-width="2"/></svg><div>Email: info@feldmoor.com</div></div>

<div class="foot-h" style="left:865px">FOLLOW US</div>
<div class="email-in">Your Email address</div>
<div class="subscribe">SUBSCRIBE</div>
<div class="social" style="left:866px"></div>
<div class="social" style="left:906px"></div>
<div class="social" style="left:943px"></div>

<div class="copyright">Copyright © 2022 Feldmoor All Right Reserved</div>

</body>
</html>
```